Curbnest - Portable Skateboard Display, Organizer, & Stand

Single Webpage for a new company that just launched our first product, the "Curbnest Skateboard Stand". This is a consumer product targeted toward parents (especially moms) with kids who have skateboards laying around. Our product is a storage/display/stand that keeps skateboards off of the ground and wheels away from walls. The website design needs to really sell the product as a Portable and Quality product, which can be put anywhere in the home. The website should appeal to adults (Moms especially) and help them quickly understand the versatility, flexibility, high quality, simplicity, and use of the Curbnest Skateboard stand. Our website can be viewed at www.curbnest-example.company - we'd like to continue to link visitors to our Vendora product listing for purchases (in the design you submit). Please review the attached creative files and feel free to reach out for additional information.

Target Market(s)

Parents (specifically Moms) with children who own skateboards, interested in keeping a clean and organized home.

Industry/Entity Type

It Company

Number of Pages Required

1 page

Font styles to use
Sans Serif

Requirements
Must have
• Must express the Portability, Quality, and Flexibility of the product. (It can be moved / placed anywhere, does not require mounting or drilling holes)
Nice to have
• Really sell the ease of use and benefit.
Should not have
• Should not be overly complex or cluttered.

```html
<!DOCTYPE html>
<html lang="en">
<head>
<meta charset="utf-8">
<title>Curbnest - Portable Skateboard Display, Organizer, &amp; Stand</title>
<link rel="stylesheet" href="https://fonts.googleapis.com/css2?family=Roboto:wght@300;400;500;700&display=swap">
<style>
:root{
  --blue:#1f62b3;
  --blue-dark:#173f78;
  --nav:#27375a;
  --nav-active:#141f36;
  --footer:#163f77;
  --footer-bottom:#0f2c55;
  --text:#555;
  --muted:#888;
  --light:#f2f3f5;
  --band:#e9ebee;
  --orange:#e8632b;
  --price:#d9342b;
  --star:#f5b400;
}
*{box-sizing:border-box;margin:0;padding:0}
html,body{width:1200px;height:2736px;overflow:hidden}
body{font-family:"Roboto",Arial,sans-serif;color:var(--text);background:#fff;font-size:13px;line-height:1.5}
.wrap{width:1030px;margin:0 auto;position:relative}

/* header */
.site-header{height:120px}
.site-header .wrap{display:flex;align-items:center;justify-content:space-between;height:120px}
.brand{display:flex;align-items:center;gap:12px;text-decoration:none}
.brand-mark{width:56px;height:56px;background:var(--blue)}
.brand-name{font-size:32px;font-weight:700;color:var(--blue);line-height:1}
.header-tools{display:flex;align-items:center;gap:8px}
.search{display:flex}
.search-field{width:200px;height:30px;border:1px solid #ccc;padding:0 8px;font-size:12px;color:var(--muted);display:flex;align-items:center}
.search-btn{width:30px;height:30px;background:#333;display:flex;align-items:center;justify-content:center}
.cart{height:30px;padding:0 12px;background:var(--blue);color:#fff;font-size:12px;display:flex;align-items:center;gap:6px}

/* nav */
.main-nav{background:var(--nav);height:40px}
.main-nav ul{list-style:none;display:flex;height:40px}
.main-nav li{flex:1;display:flex;align-items:center;justify-content:center;color:#fff;font-size:12px;font-weight:500;text-transform:uppercase;border-right:1px solid rgba(255,255,255,.12)}
.main-nav li.active{background:var(--nav-active);flex:0 0 80px}

/* hero */
.hero{height:540px;position:relative}
.hero-photo{position:absolute;inset:0;background:linear-gradient(100deg,#5a4a3c 0%,#8a7a68 30%,#c9c3b8 55%,#9a6b44 75%,#6b4a30 100%)}
.hero-caption{position:absolute;right:150px;top:215px;color:#fff}
.hero-caption h1{font-size:54px;font-weight:700;letter-spacing:1px;line-height:1.1}
.hero-caption p{font-size:26px;font-weight:300}
.hero-dots{position:absolute;bottom:22px;left:0;right:0;display:flex;justify-content:center;gap:10px}
.hero-dots span{width:10px;height:10px;border-radius:50%;background:rgba(255,255,255,.55)}
.hero-dots span.on{background:#fff}

/* welcome */
.welcome{padding:56px 0 0;text-align:center}
.section-title{font-size:22px;font-weight:500;color:#555;text-transform:uppercase}
.section-title b{color:var(--blue);font-weight:500}
.welcome p{margin-top:16px;font-size:12px;color:var(--muted);line-height:1.6;text-align:center}

/* products */
.products{margin-top:80px;background:linear-gradient(#fff,#f4f5f7 30%,#eef0f2);padding:32px 0 50px}
.bar-title{display:flex;justify-content:space-between;align-items:center;border-bottom:1px solid #ddd;padding-bottom:12px}
.bar-title h2{font-size:17px;font-weight:500;color:var(--blue);text-transform:uppercase}
.arrows{display:flex;gap:2px}
.arrows span{width:18px;height:18px;background:#555}
.product-grid{display:flex;gap:20px;justify-content:center;margin-top:40px}
.product-card{width:215px;height:245px;background:#fff;border:1px solid #dde;box-shadow:0 1px 3px rgba(0,0,0,.08);padding:10px}
.product-img{height:160px;border:1px solid #eee}
.product-meta{display:flex;justify-content:space-between;align-items:flex-end;margin-top:14px}
.product-name{font-size:12px;color:var(--blue)}
.product-price{font-size:12px;color:var(--price)}
.add-btn{background:var(--orange);color:#fff;font-size:10px;padding:4px 8px}

/* features */
.features{display:flex;gap:40px;justify-content:center;margin-top:60px}
.feature{width:300px;text-align:center}
.feature-img{height:170px}
.feature h3{font-size:14px;font-weight:500;color:var(--blue);margin-top:14px}

/* video band */
.video-band{margin-top:110px;background:var(--band);height:400px;padding-top:28px}
.video-band .wrap{display:flex;gap:36px}
.video{width:500px;height:330px;position:relative;background:linear-gradient(#3a3a3a,#1b1b1b)}
.video-play{position:absolute;left:226px;top:140px;width:48px;height:48px;border-radius:50%;background:rgba(255,255,255,.85);display:flex;align-items:center;justify-content:center}
.video-controls{position:absolute;left:0;right:0;bottom:0;height:28px;background:rgba(0,0,0,.7);display:flex;align-items:center;padding:0 10px;gap:10px}
.video-track{flex:1;height:4px;background:#777}
.video-track i{display:block;width:18%;height:4px;background:#ddd}
.video-copy{flex:1;padding-top:22px}
.video-copy h2{font-size:17px;font-weight:500;color:var(--blue);text-transform:uppercase}
.video-copy p{margin-top:14px;font-size:12px;line-height:1.6}
.video-copy ul{list-style:none;margin-top:16px}
.video-copy li{font-size:12px;padding:6px 0 6px 16px;position:relative}
.video-copy li:before{content:"";position:absolute;left:0;top:13px;width:6px;height:6px;border-radius:50%;background:var(--blue)}

/* reviews */
.reviews{padding-top:40px;height:260px;text-align:center}
.reviews h2{font-size:24px;font-weight:400;color:var(--blue);text-transform:uppercase}
.review-row{display:flex;justify-content:space-between;margin-top:30px;text-align:left}
.review{width:480px;display:flex;gap:18px}
.avatar{width:70px;height:70px;border-radius:50%;background:linear-gradient(#cfd6de,#9aa6b3);flex:none}
.review p{font-size:11px;color:var(--muted);line-height:1.6}
.review-foot{display:flex;align-items:center;gap:24px;margin-top:8px}
.reviewer b{display:block;font-size:11px;color:var(--orange);font-weight:500}
.reviewer span{font-size:10px;color:var(--muted)}
.stars{color:var(--star);font-size:18px;letter-spacing:2px}

/* footer */
.site-footer{background:var(--footer);height:232px;color:#cfd9e8;padding-top:34px}
.site-footer .wrap{display:flex;gap:40px}
.foot-col{flex:1}
.foot-col h4{font-size:13px;font-weight:500;color:#fff;text-transform:uppercase;margin-bottom:14px}
.foot-col p,.foot-col li{font-size:11px;line-height:1.7}
.foot-col ul{list-style:none}
.foot-col li:before{content:"\203A  ";}
.vendor-name{font-size:26px;font-weight:700;color:#fff;margin-top:16px}
.news-form{display:flex;margin-top:10px}
.news-field{width:150px;height:28px;background:#fff;color:#999;font-size:11px;padding:0 8px;display:flex;align-items:center}
.news-btn{height:28px;padding:0 12px;background:var(--blue-dark);color:#fff;font-size:11px;display:flex;align-items:center;border:1px solid #4a70a8}
.socials{display:flex;gap:10px;margin-top:16px;padding-left:20px}
.socials span{width:26px;height:26px;border:1px solid #7f9bc4}
.footer-bottom{background:var(--footer-bottom);height:64px}
.footer-bottom .wrap{display:flex;justify-content:space-between;align-items:center;height:64px;color:#cfd9e8;font-size:11px}
.cards{display:flex;gap:6px}
.cards span{width:34px;height:22px;background:#e8ecf2;border-radius:2px}
</style>
</head>
<body>

<header class="site-header">
  <div class="wrap">
    <a class="brand" href="#"><span class="brand-mark"></span><span class="brand-name">Curbnest</span></a>
    <div class="header-tools">
      <div class="search">
        <div class="search-field">Search</div>
        <div class="search-btn"><svg width="14" height="14" viewBox="0 0 14 14"><circle cx="6" cy="6" r="4.5" fill="none" stroke="#fff" stroke-width="1.6"/><line x1="9.3" y1="9.3" x2="13" y2="13" stroke="#fff" stroke-width="1.8"/></svg></div>
      </div>
      <div class="cart"><svg width="14" height="12" viewBox="0 0 14 12"><path d="M0 1h2.5l2 7h7l2-5H4" fill="none" stroke="#fff" stroke-width="1.3"/><circle cx="5.5" cy="10.5" r="1.2" fill="#fff"/><circle cx="10.5" cy="10.5" r="1.2" fill="#fff"/></svg>0 item(s) - $0.00</div>
    </div>
  </div>
</header>

<nav class="main-nav">
  <div class="wrap">
    <ul>
      <li class="active">Home</li><li>About Us</li><li>Services</li><li>Products</li><li>Our Brands</li><li>Wholesale</li><li>Contact Us</li>
    </ul>
  </div>
</nav>

<section class="hero">
  <div class="hero-photo" role="img" aria-label="Skateboards standing upright in a Curbnest stand inside a home entryway"></div>
  <div class="hero-caption">
    <h1>CURBNEST</h1>
    <p>Lorem Ipsum is simply dummy text</p>
  </div>
  <div class="hero-dots"><span></span><span class="on"></span><span></span><span></span><span></span></div>
</section>

<section class="welcome">
  <div class="wrap">
    <h2 class="section-title">Welcome to <b>Curbnest</b></h2>
    <p>Lorem Ipsum has been the industry's standard dummy text ever since the 1500s, when an unknown printer took a galley of type and scrambled it to make a type specimen book. It has survived not only five centuries but also the leap into electronic typesetting, remaining essentially unchanged. It was popularised in the 1960s with the release of sheets containing Lorem Ipsum passages, and more recently with desktop publishing software including versions of Lorem Ipsum.</p>
  </div>
</section>

<section class="products">
  <div class="wrap">
    <div class="bar-title"><h2>Storage Area for Accessories</h2><div class="arrows"><span></span><span></span></div></div>
    <div class="product-grid">
      <div class="product-card"><div class="product-img" role="img" aria-label="Red Curbnest stand holding a skateboard" style="background:linear-gradient(#fff 40%,#e04a5a)"></div><div class="product-meta"><div><div class="product-name">Product Name</div><div class="product-price">$19.99</div></div><span class="add-btn">Add to Basket</span></div></div>
      <div class="product-card"><div class="product-img" role="img" aria-label="Green Curbnest stand holding a skateboard" style="background:linear-gradient(#fff 40%,#8fd34a)"></div><div class="product-meta"><div><div class="product-name">Product Name</div><div class="product-price">$19.99</div></div><span class="add-btn">Add to Basket</span></div></div>
      <div class="product-card"><div class="product-img" role="img" aria-label="Cream Curbnest stand holding a skateboard" style="background:linear-gradient(#fff 40%,#e9e1c8)"></div><div class="product-meta"><div><div class="product-name">Product Name</div><div class="product-price">$19.99</div></div><span class="add-btn">Add to Basket</span></div></div>
      <div class="product-card"><div class="product-img" role="img" aria-label="Grey Curbnest stand holding a skateboard" style="background:linear-gradient(#fff 40%,#a9adb3)"></div><div class="product-meta"><div><div class="product-name">Product Name</div><div class="product-price">$19.99</div></div><span class="add-btn">Add to Basket</span></div></div>
    </div>
  </div>
</section>

<section class="features wrap">
  <div class="feature"><div class="feature-img" role="img" aria-label="Skateboard held upright by the stand in a hallway" style="background:linear-gradient(110deg,#7a6450,#cbbfae,#8c7a66)"></div><h3>Keep Boards Off The Ground</h3></div>
  <div class="feature"><div class="feature-img" role="img" aria-label="Curbnest Skateboard Stand next to a wooden dresser" style="background:linear-gradient(110deg,#c8c2b8,#7a5a3e,#b9b1a4)"></div><h3>Curbnest Skateboard Stand</h3></div>
  <div class="feature"><div class="feature-img" role="img" aria-label="Stand with boards carried to a bright room" style="background:linear-gradient(110deg,#d8d4cc,#a89a86,#e3ded6)"></div><h3>Portable and easy to move</h3></div>
</section>

<section class="video-band">
  <div class="wrap">
    <div class="video" role="img" aria-label="Product video showing a skateboard placed into the stand">
      <div class="video-play"><svg width="18" height="20" viewBox="0 0 18 20"><path d="M2 1l15 9-15 9z" fill="#333"/></svg></div>
      <div class="video-controls"><svg width="10" height="12" viewBox="0 0 10 12"><path d="M0 0l10 6-10 6z" fill="#fff"/></svg><div class="video-track"><i></i></div><svg width="14" height="12" viewBox="0 0 14 12"><rect x="1" y="1" width="12" height="10" fill="none" stroke="#fff"/></svg></div>
    </div>
    <div class="video-copy">
      <h2>Keeps Dirty Wheels Away From Walls</h2>
      <p>Lorem Ipsum has been the industry's standard dummy text ever since the 1500s, when an unknown printer took a galley of type and scrambled it to make a type specimen book. It has survived not only five centuries.</p>
      <ul>
        <li>Lorem Ipsum is simply dummy text of the printing</li>
        <li>It has survived not only five centuries</li>
        <li>Neque porro quisquam est qui dolorem</li>
        <li>Lorem Ipsum is simply dummy text of the printing</li>
      </ul>
    </div>
  </div>
</section>

<section class="reviews">
  <div class="wrap">
    <h2>Customer Reviews</h2>
    <div class="review-row">
      <div class="review"><div class="avatar" role="img" aria-label="Customer portrait"></div><div><p>&ldquo; Lorem Ipsum has been the industry's standard dummy text ever since the 1500s, when an unknown printer took a galley of type and scrambled it to make a type specimen book. &rdquo;</p><div class="review-foot"><div class="reviewer"><b>DANIEL REYES</b><span>Marketing Executive</span></div><div class="stars">★★★★★</div></div></div></div>
      <div class="review"><div class="avatar" role="img" aria-label="Customer portrait"></div><div><p>&ldquo; Lorem Ipsum has been the industry's standard dummy text ever since the 1500s, when an unknown printer took a galley of type and scrambled it to make a type specimen book. &rdquo;</p><div class="review-foot"><div class="reviewer"><b>MARA LOWELL</b><span>Marketing Executive</span></div><div class="stars">★★★★★</div></div></div></div>
    </div>
  </div>
</section>

<footer class="site-footer">
  <div class="wrap">
    <div class="foot-col"><h4>Text Widget</h4><p>Curbnest helps you to quickly and easily keep boards tidy anywhere at home.</p><div class="vendor-name">Vendora</div></div>
    <div class="foot-col"><h4>Links</h4><ul><li>Customer Support</li><li>Documentation</li><li>Resources</li><li>Shared Files</li><li>Wholesale</li></ul></div>
    <div class="foot-col"><h4>Get In Touch</h4><p>Address : 1200 Maple Row, Suite 4,<br>Northfield, NJ</p><p>Phone : (555) 014-7720</p><p>Email : hello@curbnest-example.company</p></div>
    <div class="foot-col"><h4>Newsletter</h4><p>Get our latest news and offers straight to your inbox.</p><div class="news-form"><div class="news-field">Email address</div><div class="news-btn">Submit</div></div><div class="socials"><span></span><span></span><span></span></div></div>
  </div>
</footer>
<div class="footer-bottom">
  <div class="wrap"><div class="cards"><span></span><span></span><span></span><span></span><span></span></div><div>Copyright &copy; 2015. All Rights Reserved</div></div>
</div>

</body>
</html>
```